Nur Briefpapier und VK für Pflegedienst, Logo vorhanden!!!!
Zielgruppe
Wir sind ein Pflegedienst, unsere Zielgruppe sind Krankenkassen und Patienten und andere Krankenhäuser mit denen wir zusammen arbeiten.
Aufgabenstellung
modern, seriös, elitär

```html
<!DOCTYPE html>
<html lang="de">
<head>
<meta charset="utf-8">
<title>Fenrokare Pflegedienste – Visitenkarten</title>
<link href="https://fonts.googleapis.com/css2?family=Roboto:wght@300;400;500;700&display=swap" rel="stylesheet">
<style>
  :root{
    --brand-red:#e31e24;
    --brand-red-deep:#c00d14;
    --ink:#1d1d1b;
    --paper:#ffffff;
    --stage:#e9e9e9;
    --canvas:#ffffff;
    --edge:#d6d6d6;
  }
  html,body{margin:0;padding:0;overflow:hidden;}
  body{width:1196px;height:1200px;background:var(--canvas);position:relative;font-family:"Roboto",Arial,sans-serif;}
  .stage{position:absolute;left:12px;width:734px;height:576px;background:var(--stage);display:flex;align-items:center;justify-content:center;gap:24px;}
  .stage--curves{top:12px;}
  .stage--tabs{top:600px;}
  .stage .card{width:340px;height:221px;}
  .card{position:absolute;background:var(--paper);box-shadow:0 0 0 1px var(--edge);}
  .stage .card{position:relative;}
  .card svg{display:block;width:100%;height:100%;}
  .col{left:762px;width:423px;height:276px;}
  .c1{top:12px}.c2{top:311px}.c3{top:611px}.c4{top:911px}
  .brand-name{font-family:"Roboto",Arial,sans-serif;font-weight:700;}
  .brand-tag{font-family:"Roboto",Arial,sans-serif;font-weight:300;}
  .person{font-family:"Roboto",Arial,sans-serif;fill:var(--ink);}
  .red{fill:var(--brand-red);}
  .deep{fill:var(--brand-red-deep);}
</style>
</head>
<body>

<!-- curve series: flat presentation -->
<div class="stage stage--curves">
  <div class="card">
    <svg viewBox="0 0 423 275" aria-label="Vorderseite Welle">
      <path class="deep" d="M0,195 C120,232 300,232 423,162 L423,200 C320,255 120,262 0,226 Z"/>
      <path class="red" d="M70,222 C200,248 320,246 390,232 C320,252 190,258 70,222 Z"/>
      <rect class="red" x="200" y="38" width="22" height="22"/>
      <text class="brand-name red" x="211.5" y="110" font-size="32" text-anchor="middle">Fenrokare</text>
      <text class="brand-tag red" x="211.5" y="138" font-size="16" text-anchor="middle">Pflegedienste</text>
    </svg>
  </div>
  <div class="card">
    <svg viewBox="0 0 423 275" aria-label="Rückseite Welle">
      <path class="deep" d="M68,0 C200,2 270,70 310,170 C345,250 390,270 423,272 L423,258 C380,250 355,220 330,160 C295,70 230,4 120,0 Z"/>
      <path class="red" d="M165,0 C240,20 280,90 305,170 C330,240 370,268 423,275 L395,275 C340,260 310,220 290,160 C265,80 230,20 165,0 Z"/>
      <rect class="red" x="343" y="30" width="16" height="16"/>
      <text class="brand-name red" x="351" y="80" font-size="20" text-anchor="middle">Fenrokare</text>
      <text class="brand-tag red" x="351" y="100" font-size="12" text-anchor="middle">Pflegedienste</text>
      <text class="person" x="28" y="154" font-size="14.5" font-weight="500">Jonas Beispiel</text>
      <text class="person" x="28" y="168" font-size="11.5">Pflegefachkraft</text>
      <rect class="red" x="28" y="180" width="142" height="1.5"/>
      <text class="person" x="28" y="203" font-size="11.5">Lindenweg 42</text>
      <text class="person" x="28" y="219" font-size="11.5">45127 Essen</text>
      <text class="person" x="28" y="235" font-size="11.5">Tel.: 0201 - 55 20 318</text>
      <text class="person" x="28" y="251" font-size="11.5">Email: info@fenrokare.de</text>
    </svg>
  </div>
</div>

<!-- tab series: flat presentation -->
<div class="stage stage--tabs">
  <div class="card">
    <svg viewBox="0 0 423 275" aria-label="Vorderseite Lasche">
      <path class="red" d="M151,0 H270 V232 L210.5,248 L151,232 Z"/>
      <rect fill="#fff" x="200" y="36" width="21" height="21"/>
      <text class="brand-name" fill="#fff" x="210.5" y="110" font-size="21" text-anchor="middle">Fenrokare</text>
      <text class="brand-tag" fill="#fff" x="210.5" y="206" font-size="14" text-anchor="middle">Pflegedienste</text>
    </svg>
  </div>
  <div class="card">
    <svg viewBox="0 0 423 275" aria-label="Rückseite Lasche">
      <path class="red" d="M279,0 H382 V180 L330.5,195 L279,180 Z"/>
      <rect fill="#fff" x="321" y="28" width="19" height="19"/>
      <text class="brand-name" fill="#fff" x="330.5" y="95" font-size="18" text-anchor="middle">Fenrokare</text>
      <text class="brand-tag" fill="#fff" x="330.5" y="160" font-size="13" text-anchor="middle">Pflegedienste</text>
      <text class="person" x="38" y="154" font-size="14.5" font-weight="500">Jonas Beispiel</text>
      <text class="person" x="38" y="168" font-size="11.5">Pflegefachkraft</text>
      <rect class="red" x="38" y="180" width="142" height="1.5"/>
      <text class="person" x="38" y="203" font-size="11.5">Lindenweg 42</text>
      <text class="person" x="38" y="219" font-size="11.5">45127 Essen</text>
      <text class="person" x="38" y="235" font-size="11.5">Tel.: 0201 - 55 20 318</text>
      <text class="person" x="38" y="251" font-size="11.5">Email: info@fenrokare.de</text>
    </svg>
  </div>
</div>

<!-- right column: card faces -->
<div class="card col c1">
  <svg viewBox="0 0 423 275" aria-label="Vorderseite Welle">
    <path class="deep" d="M0,195 C120,232 300,232 423,162 L423,200 C320,255 120,262 0,226 Z"/>
    <path class="red" d="M70,222 C200,248 320,246 390,232 C320,252 190,258 70,222 Z"/>
    <rect class="red" x="200" y="38" width="22" height="22"/>
    <text class="brand-name red" x="211.5" y="110" font-size="32" text-anchor="middle">Fenrokare</text>
    <text class="brand-tag red" x="211.5" y="138" font-size="16" text-anchor="middle">Pflegedienste</text>
  </svg>
</div>

<div class="card col c2">
  <svg viewBox="0 0 423 275" aria-label="Rückseite Welle">
    <path class="deep" d="M68,0 C200,2 270,70 310,170 C345,250 390,270 423,272 L423,258 C380,250 355,220 330,160 C295,70 230,4 120,0 Z"/>
    <path class="red" d="M165,0 C240,20 280,90 305,170 C330,240 370,268 423,275 L395,275 C340,260 310,220 290,160 C265,80 230,20 165,0 Z"/>
    <rect class="red" x="343" y="30" width="16" height="16"/>
    <text class="brand-name red" x="351" y="80" font-size="20" text-anchor="middle">Fenrokare</text>
    <text class="brand-tag red" x="351" y="100" font-size="12" text-anchor="middle">Pflegedienste</text>
    <text class="person" x="28" y="154" font-size="14.5" font-weight="500">Jonas Beispiel</text>
    <text class="person" x="28" y="168" font-size="11.5">Pflegefachkraft</text>
    <rect class="red" x="28" y="180" width="142" height="1.5"/>
    <text class="person" x="28" y="203" font-size="11.5">Lindenweg 42</text>
    <text class="person" x="28" y="219" font-size="11.5">45127 Essen</text>
    <text class="person" x="28" y="235" font-size="11.5">Tel.: 0201 - 55 20 318</text>
    <text class="person" x="28" y="251" font-size="11.5">Email: info@fenrokare.de</text>
  </svg>
</div>

<div class="card col c3">
  <svg viewBox="0 0 423 275" aria-label="Vorderseite Lasche">
    <path class="red" d="M151,0 H270 V232 L210.5,248 L151,232 Z"/>
    <rect fill="#fff" x="200" y="36" width="21" height="21"/>
    <text class="brand-name" fill="#fff" x="210.5" y="110" font-size="21" text-anchor="middle">Fenrokare</text>
    <text class="brand-tag" fill="#fff" x="210.5" y="206" font-size="14" text-anchor="middle">Pflegedienste</text>
  </svg>
</div>

<div class="card col c4">
  <svg viewBox="0 0 423 275" aria-label="Rückseite Lasche">
    <path class="red" d="M279,0 H382 V180 L330.5,195 L279,180 Z"/>
    <rect fill="#fff" x="321" y="28" width="19" height="19"/>
    <text class="brand-name" fill="#fff" x="330.5" y="95" font-size="18" text-anchor="middle">Fenrokare</text>
    <text class="brand-tag" fill="#fff" x="330.5" y="160" font-size="13" text-anchor="middle">Pflegedienste</text>
    <text class="person" x="38" y="154" font-size="14.5" font-weight="500">Jonas Beispiel</text>
    <text class="person" x="38" y="168" font-size="11.5">Pflegefachkraft</text>
    <rect class="red" x="38" y="180" width="142" height="1.5"/>
    <text class="person" x="38" y="203" font-size="11.5">Lindenweg 42</text>
    <text class="person" x="38" y="219" font-size="11.5">45127 Essen</text>
    <text class="person" x="38" y="235" font-size="11.5">Tel.: 0201 - 55 20 318</text>
    <text class="person" x="38" y="251" font-size="11.5">Email: info@fenrokare.de</text>
  </svg>
</div>

</body>
</html>
```